Technology Project Portal - Project Listing portal

We require a logo & website designed for our new project.

Project Name: lumrik
Description:
We have a webapp where clients and service providers can come, signup and register development projects. Service providers can the browse projects and contact clients via the portal

Design brief:
Clean & Modern - See Attached color palet & style references. (Feel free to try alternative color palets)

See Project Proposal for site requirements.
UX flow section details pages requires

Examples of all standard UI Components required e.g.
text box / field
Drop down
date picker
etc..
Updates

Target Market(s)

Business / Technology providers

Logo Text

LumRik

Coding

Coded - Design and coding required

Number of Pages Required

5+ page

Requirements
Must have
• Clean Modern Design
Examples for all common UI elements
Templates for common Web App Dialogs e.g. Confirm Delete/Logout etc

```html
<!DOCTYPE html>
<html lang="en">
<head>
<meta charset="utf-8">
<title>LumRik – Screens</title>
<link href="https://fonts.googleapis.com/css2?family=Quicksand:wght@400;500;700&family=Roboto:wght@400;500&display=swap" rel="stylesheet">
<style>
  :root{
    --brand:#ff3c00;
    --board-grey:#838288;
    --board-grey-dark:#7a797e;
    --white:#ffffff;
    --ink:#1d1d1f;
    --ink-soft:#555558;
    --muted:#9a9a9d;
    --line:#cfcfd2;
    --photo-deep:#1c3358;
    --photo-mid:#3a6fa8;
    --photo-warm:#d98a55;
    --illu-grey:#e6e6e8;
  }
  *{box-sizing:border-box;margin:0;padding:0}
  html,body{width:691px;height:1200px;overflow:hidden;background:var(--white)}
  body{position:relative;font-family:"Quicksand",sans-serif;color:var(--ink)}

  .board{position:absolute;left:30px;width:631px;height:343px;background:var(--white);
    box-shadow:0 0 4px rgba(0,0,0,.12)}
  .board__band{position:absolute;left:0;top:0;width:242px;height:100%;
    background:linear-gradient(180deg,var(--board-grey),var(--board-grey-dark))}
  .board--signup{top:41px}
  .board--landing{top:421px}
  .board--listing{top:802px}

  .card{position:absolute;left:82px;top:47px;width:466px;height:250px;background:var(--white);
    box-shadow:0 6px 18px rgba(0,0,0,.22);overflow:hidden}
  .card__brand-side{position:absolute;left:0;top:0;width:160px;height:100%;background:var(--brand)}

  .wordmark{position:absolute;display:flex;align-items:center;gap:4px;
    font-family:"Quicksand",sans-serif;font-weight:700;letter-spacing:1px;color:var(--white)}
  .wordmark__dot{width:12px;height:12px;border-radius:50%;background:var(--white)}
  .wordmark--orange{color:var(--brand)}
  .wordmark--orange .wordmark__dot{background:var(--brand)}

  /* sign-up form */
  .existing{position:absolute;right:14px;top:10px;font-family:"Roboto",sans-serif;font-size:4px;color:var(--ink)}
  .existing a{color:var(--brand);text-decoration:none}
  .form-title{position:absolute;left:262px;width:138px;top:41px;text-align:center;
    font-family:"Roboto",sans-serif;font-size:11.5px;color:var(--ink)}
  .tabs{position:absolute;left:262px;top:64px;width:138px;height:17px;border-bottom:0.6px solid var(--ink-soft);
    display:flex;font-family:"Roboto",sans-serif;font-size:6.5px}
  .tab{flex:0 0 71px;text-align:center;color:var(--muted)}
  .tab--active{color:var(--brand);font-weight:500;border-bottom:1px solid var(--brand);margin-bottom:-0.6px}
  .tab:last-child{flex:1 1 auto}
  .field-label{position:absolute;left:262px;font-family:"Roboto",sans-serif;font-size:4.6px;font-weight:500;color:var(--ink)}
  .field{position:absolute;left:262px;width:138px;height:14.5px;border:0.6px solid var(--line);
    font-family:"Roboto",sans-serif;font-size:3.8px;color:var(--muted);padding:0 4px;line-height:13.5px}
  .btn{position:absolute;display:flex;align-items:center;justify-content:center;gap:5px;
    font-family:"Roboto",sans-serif;font-size:7.4px;border-radius:1px}
  .btn--primary{background:var(--brand);color:var(--white);box-shadow:0 3px 6px rgba(255,60,0,.25)}
  .btn--outline-brand{background:var(--white);color:var(--brand);border:0.7px solid var(--brand);box-shadow:0 2px 5px rgba(0,0,0,.15)}
  .btn--outline{background:var(--white);color:var(--ink);border:0.7px solid var(--ink)}

  /* landing */
  .illustration{position:absolute;left:13px;top:86px;width:137px;height:72px;
    background:linear-gradient(90deg,var(--illu-grey) 0 28%,rgba(255,255,255,.15) 28% 34%,#f4f4f6 34% 70%,rgba(255,255,255,.15) 70% 82%,#3f4468 82% 96%,transparent 96%);
    opacity:.9;border-bottom:0.6px solid #3f4468}
  .hero-title{position:absolute;left:188px;top:83px;font-family:"Quicksand",sans-serif;font-weight:700;
    font-size:16px;letter-spacing:1.5px;color:var(--ink)}
  .hero-text{position:absolute;left:188px;top:107px;width:244px;font-size:8px;line-height:13.6px;color:var(--ink-soft)}

  /* listing */
  .photo{position:absolute;left:33px;top:45px;width:405px;height:85px;
    background:linear-gradient(180deg,#c9a7a0 0%,var(--photo-mid) 35%,var(--photo-deep) 70%,#2b2238 85%,var(--photo-warm) 100%)}
  .listing-text{position:absolute;left:33px;top:142px;width:410px;font-size:7.6px;line-height:12.6px;color:var(--ink-soft)}
</style>
</head>
<body>

<section class="board board--signup">
  <div class="board__band"></div>
  <div class="card">
    <div class="card__brand-side">
      <div class="wordmark" style="left:23px;top:111px;font-size:16px"><span class="wordmark__dot"></span>LUMRIK</div>
    </div>
    <p class="existing">Existing User? Click here to <a href="#">Sign in</a></p>
    <h1 class="form-title">Create An Account</h1>
    <div class="tabs"><span class="tab tab--active">Client</span><span class="tab">Service</span></div>
    <label class="field-label" style="top:94px">NAME</label>
    <div class="field" style="top:102px">Enter your name</div>
    <label class="field-label" style="top:123px">EMAIL</label>
    <div class="field" style="top:131px">Enter your mail</div>
    <label class="field-label" style="top:152px">PASSWORD</label>
    <div class="field" style="top:160px">Enter your password</div>
    <div class="btn btn--primary" style="left:283px;top:184px;width:93px;height:19px">Next &rarr;</div>
  </div>
</section>

<section class="board board--landing">
  <div class="board__band"></div>
  <div class="card">
    <div class="card__brand-side">
      <div class="wordmark" style="left:23px;top:17px;font-size:16px"><span class="wordmark__dot"></span>LUMRIK</div>
      <div class="illustration" role="img" aria-label="Illustration of a person standing beside a large tablet showing a project form, with a plant"></div>
    </div>
    <div class="btn btn--outline-brand" style="left:362px;top:9.5px;width:67px;height:18.5px">Login
      <svg width="8" height="9" viewBox="0 0 8 9" aria-hidden="true"><circle cx="4" cy="2.3" r="2.1" fill="#ff3c00"/><path d="M0 9 C0 5 8 5 8 9Z" fill="#ff3c00"/></svg>
    </div>
    <h2 class="hero-title">LUMRIK</h2>
    <p class="hero-text">Sed ut perspiciatis unde omnis iste natus error sit voluptatemawe accusantium doloremque laudantium, totam rem aperiam, eaque ipsa quae ab illo inventore veritatis et quasi architecto beatae vitae dicta sunt explicabo.</p>
    <div class="btn btn--primary" style="left:361px;top:193px;width:67px;height:19px">Sign Up
      <svg width="9" height="9" viewBox="0 0 9 9" aria-hidden="true" fill="none" stroke="#fff" stroke-width="0.9"><path d="M3 3H1V8.5H8V3H6"/><path d="M4.5 6V0.7M2.8 2.2L4.5 0.7 6.2 2.2"/></svg>
    </div>
  </div>
</section>

<section class="board board--listing">
  <div class="board__band"></div>
  <div class="card">
    <div class="wordmark wordmark--orange" style="left:29px;top:18px;font-size:13px"><span class="wordmark__dot"></span>LUMRIK</div>
    <div class="photo" role="img" aria-label="Photo of a businessman seen from behind overlooking a night city skyline with glowing network lines"></div>
    <p class="listing-text">Sed ut perspiciatis unde omnis iste natus error sit voluptatemawe accusantium doloremque laudantium, totam rem aperiam, eaque ipsa quae ab illo inventore veritatis et quasi architecto beatae vitae dicta sunt explicabo.</p>
    <div class="btn btn--outline" style="left:33px;top:183px;width:67px;height:19px">Free</div>
    <div class="btn btn--outline" style="left:108px;top:182px;width:67px;height:19px">$$$ Paid</div>
    <div class="btn btn--primary" style="left:370px;top:207px;width:67px;height:19px;box-shadow:none">Save</div>
  </div>
</section>

</body>
</html>
```